Business Card for Academic Coach

I need a business card designed for me - a private tutor/academic coach.

Glen Mabery
Academic Coach
AB Pellwood University, 1994 Cum Laude
Phone: 404-555-0187
glenrmabery@tutormail-example.com

Subjects
QET and BRT
Math, Physics, Writing

```html
<!DOCTYPE html>
<html lang="en">
<head>
<meta charset="utf-8">
<title>Glen Mabery – Academic Coach Business Card</title>
<link href="https://fonts.googleapis.com/css2?family=Questrial&display=swap" rel="stylesheet">
<style>
  :root {
    --backdrop: #1b1b1b;
    --card: #efefef;
    --ink: #2e2e2e;
    --ink-soft: #3a3a3a;
    --orange: #f1501f;
    --red: #ec2c2b;
  }
  * { margin: 0; padding: 0; box-sizing: border-box; }
  html, body {
    width: 1200px;
    height: 900px;
    overflow: hidden;
    background: var(--backdrop);
    font-family: "Questrial", "Helvetica Neue", Arial, sans-serif;
    color: var(--ink);
  }
  .canvas { position: relative; width: 1200px; height: 900px; }
  .card {
    position: absolute;
    top: 33px;
    width: 520px;
    height: 834px;
    background: var(--card);
    overflow: hidden;
  }
  .card--front { left: 38px; }
  .card--back { left: 630px; }

  .accent-corner {
    position: absolute;
    top: 0;
    left: 195px;
    width: 325px;
    height: 181px;
    background: linear-gradient(90deg, var(--orange) 0%, var(--red) 100%);
  }

  .line {
    position: absolute;
    left: 0;
    width: 100%;
    text-align: center;
    transform: translateY(-50%);
    white-space: nowrap;
  }
  .name { top: 234px; font-size: 44px; font-weight: 400; letter-spacing: 1.5px; }
  .role { top: 281px; font-size: 23px; letter-spacing: 0.5px; color: var(--ink-soft); }
  .icon { position: absolute; left: 50%; transform: translate(-50%, -50%); fill: var(--ink); }
  .icon--home { top: 417px; width: 64px; height: 60px; }
  .icon--phone { top: 564px; width: 62px; height: 56px; }
  .icon--mail { top: 708px; width: 60px; height: 50px; }
  .detail { font-size: 25px; color: var(--ink-soft); }
  .detail--degree { top: 477px; font-size: 25px; }
  .detail--phone { top: 616px; }
  .detail--email { top: 759px; font-size: 23px; }

  .subject { font-size: 52px; color: var(--ink-soft); letter-spacing: 0.5px; }
  .subject--tests { top: 234px; }
  .subject--math { top: 353px; }
  .subject--physics { top: 474px; }
  .subject--writing { top: 594px; }
  .divider { font-size: 22px; letter-spacing: 1px; color: var(--ink-soft); }
  .divider--1 { top: 289px; }
  .divider--2 { top: 411px; }
  .divider--3 { top: 534px; }
</style>
</head>
<body>
<main class="canvas">
  <section class="card card--front" aria-label="Card front">
    <div class="accent-corner" role="img" aria-label="Decorative orange and red folded-ribbon artwork in the top corner"></div>

    <h1 class="line name">GLEN MABERY</h1>
    <p class="line role">ACADEMIC COACH</p>

    <svg class="icon icon--home" viewBox="0 0 64 60" aria-hidden="true">
      <polygon points="32,2 2,30 8,30 32,8 56,30 62,30"/>
      <rect x="44" y="6" width="7" height="14"/>
      <path d="M11 30 L32 11 L53 30 V58 H11 Z M27 38 V58 H37 V38 Z" fill-rule="evenodd"/>
    </svg>
    <p class="line detail detail--degree">AB Pellwood University, 1994 Cum Laude</p>

    <svg class="icon icon--phone" viewBox="0 0 62 56" aria-hidden="true">
      <path d="M2 16 C2 6 14 2 31 2 C48 2 60 6 60 16 V20 H46 V13 H16 V20 H2 Z"/>
      <path d="M14 22 H48 L56 40 V54 H6 V40 Z"/>
      <g fill="var(--card)">
        <rect x="21" y="28" width="5" height="4"/><rect x="29" y="28" width="5" height="4"/><rect x="37" y="28" width="5" height="4"/>
        <rect x="21" y="35" width="5" height="4"/><rect x="29" y="35" width="5" height="4"/><rect x="37" y="35" width="5" height="4"/>
        <rect x="21" y="42" width="5" height="4"/><rect x="29" y="42" width="5" height="4"/><rect x="37" y="42" width="5" height="4"/>
      </g>
    </svg>
    <p class="line detail detail--phone">404-555-0187</p>

    <svg class="icon icon--mail" viewBox="0 0 60 50" aria-hidden="true">
      <path d="M30 2 L58 20 V48 H2 V20 Z"/>
      <rect x="14" y="8" width="32" height="24" fill="var(--card)"/>
      <g fill="var(--ink)">
        <rect x="20" y="14" width="20" height="2.5"/><rect x="20" y="19" width="20" height="2.5"/><rect x="20" y="24" width="14" height="2.5"/>
      </g>
      <path d="M2 22 L30 38 L58 22" fill="none" stroke="var(--card)" stroke-width="2.5"/>
    </svg>
    <p class="line detail detail--email">glenrmabery@tutormail-example.com</p>
  </section>

  <section class="card card--back" aria-label="Card back: subjects">
    <p class="line subject subject--tests">QET and BRT</p>
    <p class="line divider divider--1">--------- x ---------</p>
    <p class="line subject subject--math">Math</p>
    <p class="line divider divider--2">--------- x ---------</p>
    <p class="line subject subject--physics">Physics</p>
    <p class="line divider divider--3">--------- x ---------</p>
    <p class="line subject subject--writing">Writing</p>
  </section>
</main>
</body>
</html>
```